Financial advisory firm needs new business card design

Business card design , simple , elegant, professional. Will use existing logo. One side should be a solid blue background (matching blue in Logo) . info side should have basic info, maybe two color panes. one white, one a different color..maybe light grey. Please visit our website to get feel for colors and business. www.tallowmeadwealth.com

Industry/Entity Type

Financial Service

Contact Information for Business Card

Basic info..minimalist, modern, approach

Colors

Designer to choose colors to be used in the design.

Requirements
Must have
• Important regulatory requirement. The following disclosure MUST be included somewhere on the business card. It can be either front, or back, and it may be in a smaller font (but has to be legible). My interest is to satisfy the requirement with the least possible disruption to the beauty of the card design.
• All securities offered through the Harrowgate Capital, Inc. Oakhurst Lane, NJ. Member QOLTA/DWEM. Advisory services provided through HC Advisory Services, Inc. an PBR Registered Investment Advisor.

```html
<!DOCTYPE html>
<html lang="en">
<head>
<meta charset="utf-8">
<title>Tallowmead Wealth – Business Card</title>
<link rel="stylesheet" href="https://fonts.googleapis.com/css2?family=Mulish:wght@400;800&family=Open+Sans:wght@400&display=swap">
<style>
  :root {
    --brand-blue: #0b5189;
    --accent-blue: #1a6fc0;
    --ink: #1c1c1c;
    --muted: #3a3a3a;
    --paper: #ffffff;
    --backdrop: #2a2a2c;
  }
  * { box-sizing: border-box; margin: 0; padding: 0; }
  html, body { width: 1200px; height: 900px; overflow: hidden; }
  body { background: var(--backdrop); position: relative; font-family: "Open Sans", sans-serif; }

  .card {
    position: absolute;
    width: 630px; height: 360px;
    border-radius: 26px;
    overflow: hidden;
    box-shadow: 0 18px 40px rgba(0,0,0,.45);
  }

  /* Back side */
  .card--back { left: 500px; top: 50px; background: var(--brand-blue); color: var(--paper); }
  .card--back .wordmark { position: absolute; left: 0; right: 0; top: 95px; justify-content: center; color: var(--paper); }
  .disclosure {
    position: absolute; left: 40px; right: 40px; top: 255px;
    text-align: center; font-size: 11.5px; line-height: 1.75; letter-spacing: .2px;
  }
  .disclosure .sep { color: #5aa6ea; padding: 0 5px; }

  /* Wordmark */
  .wordmark { display: flex; align-items: center; gap: 14px; }
  .wordmark__dot { width: 18px; height: 18px; border-radius: 50%; background: currentColor; flex: none; }
  .wordmark__name { font-family: "Mulish", sans-serif; font-weight: 800; font-size: 44px; letter-spacing: 1px; text-transform: uppercase; line-height: 1; }

  /* Front side */
  .card--front { left: 70px; top: 480px; background: var(--paper); color: var(--ink); }
  .card--front .wordmark { position: absolute; left: 0; right: 0; top: 70px; justify-content: center; color: var(--ink); }

  .identity { position: absolute; left: 70px; top: 185px; width: 235px; text-align: right; }
  .identity__name { font-family: "Mulish", sans-serif; font-weight: 800; font-size: 30px; color: var(--accent-blue); letter-spacing: 1px; }
  .identity__title { font-family: "Mulish", sans-serif; font-size: 19px; color: var(--muted); margin-top: 2px; }

  .divider { position: absolute; left: 325px; top: 188px; width: 2px; height: 80px; background: var(--accent-blue); }

  .contacts { position: absolute; left: 345px; top: 186px; list-style: none; }
  .contacts li { display: flex; align-items: center; gap: 10px; font-size: 15.5px; color: var(--muted); height: 27px; }
  .contacts svg { width: 14px; height: 14px; fill: var(--brand-blue); flex: none; }

  .address-band {
    position: absolute; left: 0; right: 0; bottom: 18px; height: 50px;
    background: var(--brand-blue); color: var(--paper);
    font-family: "Mulish", sans-serif; font-size: 17px;
    display: flex; align-items: center; justify-content: center;
  }
</style>
</head>
<body>

  <section class="card card--back" aria-label="Card back">
    <div class="wordmark">
      <span class="wordmark__dot"></span>
      <span class="wordmark__name">Tallowmead Wealth</span>
    </div>
    <p class="disclosure">
      All securities offered through Harrowgate Capital, Inc. Oakhurst Lane, NJ.<span class="sep">|</span>Member QOLTA/DWEM<br>
      Advisory services provided through HC Advisory Services, Inc.<span class="sep">|</span>an PBR Registered Investment Advisor.
    </p>
  </section>

  <section class="card card--front" aria-label="Card front">
    <div class="wordmark">
      <span class="wordmark__dot"></span>
      <span class="wordmark__name">Tallowmead Wealth</span>
    </div>

    <div class="identity">
      <h1 class="identity__name">Maren Ostby</h1>
      <p class="identity__title">General Manager</p>
    </div>

    <div class="divider"></div>

    <ul class="contacts">
      <li>
        <svg viewBox="0 0 24 24" aria-hidden="true"><path d="M6.6 10.8a15.1 15.1 0 0 0 6.6 6.6l2.2-2.2a1 1 0 0 1 1-.25 11.4 11.4 0 0 0 3.6.57 1 1 0 0 1 1 1V20a1 1 0 0 1-1 1A17 17 0 0 1 3 4a1 1 0 0 1 1-1h3.5a1 1 0 0 1 1 1c0 1.25.2 2.45.57 3.57a1 1 0 0 1-.25 1z"/></svg>
        844-555-0172
      </li>
      <li>
        <svg viewBox="0 0 24 24" aria-hidden="true"><path d="M3 5h18a1 1 0 0 1 1 1v12a1 1 0 0 1-1 1H3a1 1 0 0 1-1-1V6a1 1 0 0 1 1-1zm1 2.4V17h16V7.4l-8 5.3z M5.2 7 12 11.5 18.8 7z"/></svg>
        mostby@tallowmeadwealth.com
      </li>
      <li>
        <svg viewBox="0 0 24 24" aria-hidden="true"><path d="M12 2a10 10 0 1 0 0 20 10 10 0 0 0 0-20zm6.9 6h-3a15.7 15.7 0 0 0-1.3-3.6A8 8 0 0 1 18.9 8zM12 4c.8 1.2 1.5 2.5 1.9 4h-3.8c.4-1.5 1.1-2.8 1.9-4zM4.3 14a8 8 0 0 1 0-4h3.4a16 16 0 0 0 0 4zm.8 2h3a15.7 15.7 0 0 0 1.3 3.6A8 8 0 0 1 5.1 16zm3-8h-3a8 8 0 0 1 4.3-3.6A15.7 15.7 0 0 0 8.1 8zM12 20c-.8-1.2-1.5-2.5-1.9-4h3.8c-.4 1.5-1.1 2.8-1.9 4zm2.3-6H9.7a14.6 14.6 0 0 1 0-4h4.6a14.6 14.6 0 0 1 0 4zm.3 5.6a15.7 15.7 0 0 0 1.3-3.6h3a8 8 0 0 1-4.3 3.6zm1.7-5.6a16 16 0 0 0 0-4h3.4a8 8 0 0 1 0 4z"/></svg>
        www.tallowmeadwealth.com
      </li>
    </ul>

    <div class="address-band">1480 W Quarry Rd Linden Falls, Harlow County 76011 USA</div>
  </section>

</body>
</html>
```